Business card design needed

We are a start up Mobile Vet Clinic.
We will be servicing an are that cover the Gladstone Region Shire.
Bookings will be made via the number listed or email address.
Travel will be charged

Target Market(s)

Pet Owners

Industry/Entity Type

Business

Contact Information for Business Card

BRAMLEY MOBILE VET
Tavestock Pty Ltd
Nora Batterby BVSc
27 Harwick St
Kelmore QLD 4691

PH: 0738214069 Fax: 0738214552 email: bmvet@tallowmail.com

Logo styles of interest
Pictorial/Combination Logo

```html
<!DOCTYPE html>
<html lang="en">
<head>
<meta charset="utf-8">
<title>Bramley Mobile Vet — Business Card</title>
<link rel="stylesheet" href="https://fonts.googleapis.com/css2?family=Josefin+Sans:ital,wght@0,300;0,400;1,300;1,400&display=swap">
<style>
  :root {
    --card-bg: #d3fcfd;
    --emblem-tint: #e4fefe;
    --ink: #141414;
    --ink-soft: #4a4f50;
  }
  html, body {
    margin: 0;
    padding: 0;
    width: 1200px;
    height: 693px;
    overflow: hidden;
    background: var(--card-bg);
  }
  .card {
    position: relative;
    width: 1200px;
    height: 693px;
    background: var(--card-bg);
    font-family: "Josefin Sans", sans-serif;
    color: var(--ink);
    overflow: hidden;
  }
  .emblem {
    position: absolute;
    left: 478px;
    top: 86px;
    width: 250px;
    height: 520px;
    background: radial-gradient(ellipse at 50% 50%, var(--emblem-tint) 0%, rgba(228, 254, 254, 0.55) 55%, rgba(211, 252, 253, 0) 100%);
  }
  .business-name {
    position: absolute;
    left: 0;
    right: 0;
    top: 224px;
    margin: 0;
    text-align: center;
    font-weight: 400;
    font-size: 78px;
    line-height: 1;
    letter-spacing: 0.045em;
  }
  .business-name .mobile {
    font-style: italic;
    color: #262626;
  }
  .practitioner {
    position: absolute;
    left: 0;
    right: 0;
    top: 316px;
    margin: 0;
    text-align: center;
    font-weight: 300;
    font-size: 52px;
    line-height: 1;
    letter-spacing: 0.05em;
  }
  .contact {
    position: absolute;
    left: 0;
    right: 0;
    top: 496px;
    margin: 0;
    font-style: normal;
    text-align: center;
    font-size: 37px;
    line-height: 50px;
    letter-spacing: 0.02em;
  }
  .contact p { margin: 0; }
  .contact .value {
    font-style: italic;
    font-weight: 300;
    color: var(--ink);
  }
  .contact .label {
    font-weight: 300;
    color: var(--ink-soft);
  }
  .contact .email-line { font-size: 34px; }
</style>
</head>
<body>
  <main class="card">
    <div class="emblem" role="img" aria-label="Faint veterinary emblem watermark behind the text"></div>
    <h1 class="business-name">BRAMLEY <span class="mobile">MOBILE</span> VET</h1>
    <p class="practitioner">Tavestock Pty Ltd Nora Batterby BVSc</p>
    <address class="contact">
      <p class="value">27 Harwick St Kelmore QLD 4691</p>
      <p><span class="label">PH:</span> <span class="value">0738214069</span> <span class="label">Fax:</span> <span class="value">0738214552</span></p>
      <p class="email-line"><span class="label">email:</span> <span class="value">bmvet@tallowmail.com</span></p>
    </address>
  </main>
</body>
</html>
```